Anatomic 3D models + Urological Robotic surgery site

I want a website to represent my business as a developer of 3D models (reconstructions based on CT and MRI scans) and urological robotic surgery. The main point I need on my website is that it is modern, very attractive, clean, responsive and an interaction that differentiate me from the usual websites they have in my market. The site will be in portuguese and I'll provide the content to be used. The company name would be my name: Dr Rui Valmonte. The colors and other choices I made here are not final decisions. If you have a suggestion you, they are welcome.

My patients

Medical

Sans Serif

0054AA
0677BA
7BADD7
CADEEF
E8F1F8
0094D4
00A9DD
6FCCEA
C7EBF8
E9F6FB
00AB8E
00BBA5
67D7C9
C6EFE9
E9F9F6
59FF00
82FF00
B8FF75
E3FFCB
F4FFEA
FFC000
F8CF3A
FAE287
FDF2CF
FEFAEE
F0912C
F2A743
F7CA91
FBE8D2
FDF5EE
A7469A
B969AE
D3A5CF
EDDBEB
F8F0F9
6B429C
8869AF
B7A5CE
E3DAEB
F3F0F8

• Responsive, clean, modern, attractive, stand out from usual sites.
• Antiquate boring designs.

```html
<!DOCTYPE html>
<html lang="pt">
<head>
<meta charset="utf-8">
<title>Dr Rui Valmonte — Urologia e Cirurgia Minimamente Invasiva</title>
<link href="https://fonts.googleapis.com/css2?family=Lato:wght@400;700;900&family=Poppins:wght@400;500;600;700&display=swap" rel="stylesheet">
<style>
:root{
  --purple:#5b3a8e;
  --purple-deep:#4e2f82;
  --orange:#f37021;
  --orange-soft:#f7a15f;
  --ink:#1f1f24;
  --text:#2e2e33;
  --muted:#55555c;
  --cream:#faf6f2;
  --cream-deep:#f3ece4;
  --white:#ffffff;
  --grad:linear-gradient(90deg,var(--purple) 0%,var(--orange) 100%);
}
*{box-sizing:border-box;margin:0;padding:0}
html,body{width:1200px;height:3891px;overflow:hidden}
body{font-family:'Poppins',sans-serif;color:var(--text);background:var(--white);position:relative}
.abs{position:absolute}
.btn{position:absolute;display:flex;align-items:center;justify-content:center;gap:8px;border-radius:24px;background:var(--grad);color:var(--white);font-family:'Poppins',sans-serif;font-weight:700;font-size:15px;text-transform:uppercase;letter-spacing:.2px;text-decoration:none}
.btn svg{width:15px;height:15px}
.heading{font-family:'Lato',sans-serif;font-weight:700;color:var(--purple);text-transform:uppercase;letter-spacing:-.5px}

/* header */
.topline{position:absolute;left:0;top:0;width:1200px;height:4px;background:var(--purple)}
.brand{position:absolute;left:110px;top:58px;width:292px;text-align:center}
.brand-name{font-family:'Lato',sans-serif;font-weight:400;font-size:34px;color:#3a3a3e;line-height:1.1}
.brand-tag{font-size:8px;font-weight:600;letter-spacing:1.4px;color:#3a3a3e;margin-top:4px;text-transform:uppercase}
.call-icon{left:700px;top:32px;width:48px;height:48px;border-radius:50%;background:var(--white);box-shadow:0 4px 14px rgba(0,0,0,.12);display:flex;align-items:center;justify-content:center}
.call-label{left:767px;top:31px;font-size:13px;font-weight:600;color:var(--orange)}
.call-number{left:767px;top:51px;font-size:17px;font-weight:600;color:var(--purple)}
.divider-v{left:947px;top:38px;width:1px;height:34px;background:#ddd}
.social{position:absolute;width:34px;height:34px;border-radius:50%;background:var(--white);box-shadow:0 3px 10px rgba(0,0,0,.12)}
.social.active{background:var(--grad)}
.nav{position:absolute;top:107px;display:flex;font-size:15px;font-weight:500;color:var(--ink)}
.nav a{position:absolute;white-space:nowrap;color:var(--ink);text-decoration:none}
.nav a.current{color:var(--orange)}
.nav a.current::after{content:"";position:absolute;left:0;right:0;bottom:-3px;height:2px;background:var(--orange)}

/* hero */
.hero{position:absolute;left:0;top:166px;width:1200px;height:702px;overflow:hidden}
.hero-photo{position:absolute;inset:0;background:linear-gradient(115deg,#2c3a44 0%,#4d5a60 35%,#6d6a64 65%,#5a4636 100%)}
.hero-shade{position:absolute;inset:0;background:rgba(20,25,30,.35)}
.hero-title{position:absolute;left:200px;top:184px;width:800px;text-align:center;font-family:'Lato',sans-serif;font-weight:700;font-size:46px;line-height:51px;color:var(--white);text-transform:uppercase}
.hero-text{position:absolute;left:230px;top:300px;width:740px;text-align:center;font-size:19.5px;line-height:28.5px;color:var(--white)}
.arrow{position:absolute;top:284px;width:34px;height:34px;border-radius:50%;display:flex;align-items:center;justify-content:center}
.hero-wave{position:absolute;left:0;bottom:0;width:1200px;height:240px}

/* about */
.about-ring{left:110px;top:890px;width:447px;height:424px;border-radius:50%;background:linear-gradient(180deg,#fdfbf8 0%,var(--cream-deep) 100%)}
.about-photo{left:150px;top:907px;width:368px;height:368px;border-radius:50%;background:linear-gradient(160deg,#a8683a 0%,#7c4e2c 55%,#d9d6d2 100%)}
.name-badge{left:303px;top:1243px;width:292px;height:58px;border-radius:30px;background:var(--white);box-shadow:0 6px 18px rgba(0,0,0,.1);display:flex;align-items:center;padding-left:8px;gap:20px;font-size:19px;font-weight:600;color:var(--ink)}
.name-badge .dot{width:44px;height:44px;border-radius:50%;background:var(--purple);display:flex;align-items:center;justify-content:center}
.about-text{left:640px;top:885px;width:450px}
.about-text .heading{font-size:50px;line-height:60px}
.about-sub{font-size:20px;font-weight:600;color:var(--ink);margin-top:6px}
.about-text p{font-size:15.5px;line-height:25.6px;color:var(--text);margin-top:17px}
.about-text p+p{margin-top:8px}

/* como atuamos */
.approach{position:absolute;left:0;top:1420px;width:1200px;height:813px;background:var(--cream)}
.approach .heading{position:absolute;left:0;width:1200px;top:88px;text-align:center;font-size:50px}
.approach-sub{position:absolute;left:0;width:1200px;top:160px;text-align:center;font-size:20.5px;font-weight:600;color:var(--ink)}
.approach-text{position:absolute;left:140px;width:920px;top:206px;text-align:center;font-size:15.5px;line-height:25.6px}
.approach-text p+p{margin-top:6px}
.card{position:absolute;top:353px;width:297px;height:359px;border-radius:22px;background:var(--white);box-shadow:0 6px 20px rgba(0,0,0,.08);text-align:center}
.card-icon{position:absolute;left:95px;top:38px;width:106px;height:106px;border-radius:50%;background:var(--cream-deep);display:flex;align-items:center;justify-content:center}
.card-icon.filled{background:var(--orange)}
.card h3{position:absolute;left:22px;right:22px;top:172px;font-size:21px;line-height:32.5px;font-weight:600;color:var(--ink)}

/* serviços */
.services{position:absolute;left:0;top:2233px;width:1200px;height:789px;background:linear-gradient(100deg,#5a3a8e 0%,#7a4a86 35%,#c75f49 70%,#f3731f 100%)}
.services .heading{position:absolute;left:0;width:1200px;top:68px;text-align:center;font-size:50px;color:var(--white)}
.tab{position:absolute;top:160px;width:312px;height:47px;border-radius:24px;border:1.5px solid rgba(255,255,255,.8);color:var(--white);font-size:13px;font-weight:600;display:flex;align-items:center;justify-content:center;text-transform:uppercase}
.tab.active{background:var(--white);color:var(--purple)}
.tab.active::after{content:"";position:absolute;left:148px;bottom:-10px;border:8px solid transparent;border-top:9px solid var(--white);border-bottom:0}
.panel{position:absolute;left:110px;top:239px;width:978px;height:470px;background:var(--white)}
.panel .heading{position:absolute;left:42px;top:40px;width:420px;text-align:left;font-size:35px;line-height:41px;color:var(--purple)}
.panel-sub{position:absolute;left:42px;top:138px;width:400px;font-size:19px;line-height:28px;font-weight:600;font-style:italic;color:var(--ink)}
.panel-text{position:absolute;left:42px;top:196px;width:405px;font-size:15.5px;line-height:25.6px}
.panel-text p+p{margin-top:8px}
.panel-image{position:absolute;left:477px;top:25px;width:475px;height:420px;background:linear-gradient(135deg,#8a8fd6 0%,#7b7fcf 50%,#9a9ad8 100%)}

/* compromisso */
.commitment .heading{position:absolute;left:0;width:1200px;top:3117px;text-align:center;font-size:50px;line-height:56px}
.commitment-text{position:absolute;left:150px;width:900px;top:3241px;text-align:center;font-size:15.5px;line-height:25.6px}
.commitment-text p+p{margin-top:12px}

/* footer */
.footer{position:absolute;left:0;top:3520px;width:1200px;height:371px;background:var(--cream)}
.footer .brand{left:456px;top:70px;width:290px}
.footer-nav{position:absolute;left:0;width:1200px;top:152px;display:flex;justify-content:center;gap:22px;font-size:19px;font-weight:500;color:var(--ink)}
.footer-nav .sep{color:var(--ink)}
.footer-contact{position:absolute;left:0;width:1200px;top:199px;display:flex;justify-content:center;align-items:center;gap:16px;font-size:15px;color:var(--muted)}
.footer-contact span{display:flex;align-items:center;gap:10px}
.footer-rule{position:absolute;left:110px;width:978px;top:301px;height:1px;background:#ddd6ce}
.copyright{position:absolute;left:0;width:1200px;top:322px;text-align:center;font-size:13px;color:var(--text)}
</style>
</head>
<body>

<div class="topline"></div>

<header>
  <div class="brand">
    <div class="brand-name">Dr Rui Valmonte</div>
    <div class="brand-tag">Urologia e cirurgia minimamente invasiva</div>
  </div>

  <div class="abs call-icon">
    <svg width="22" height="22" viewBox="0 0 24 24" fill="none" stroke="#f37021" stroke-width="2.2" stroke-linecap="round" stroke-linejoin="round"><path d="M22 16.9v3a2 2 0 0 1-2.2 2 19.8 19.8 0 0 1-8.6-3.1 19.5 19.5 0 0 1-6-6A19.8 19.8 0 0 1 2.1 4.2 2 2 0 0 1 4.1 2h3a2 2 0 0 1 2 1.7c.1.9.4 1.8.7 2.7a2 2 0 0 1-.5 2.1L8 9.8a16 16 0 0 0 6 6l1.3-1.3a2 2 0 0 1 2.1-.4c.9.3 1.8.6 2.7.7a2 2 0 0 1 1.7 2z"/></svg>
  </div>
  <div class="abs call-label">Call Me:</div>
  <div class="abs call-number">+1 (555) 014 2290</div>
  <div class="abs divider-v"></div>
  <span class="social active" style="left:973px;top:37px"></span>
  <span class="social" style="left:1014px;top:37px"></span>
  <span class="social" style="left:1053px;top:37px"></span>

  <nav class="nav">
    <a class="current" href="#" style="left:477px">Início</a>
    <a href="#" style="left:545px">Sobre nós</a>
    <a href="#" style="left:649px">Nossos serviços</a>
    <a href="#" style="left:800px">Recursos</a>
  </nav>
  <a class="btn" href="#" style="left:905px;top:95px;width:183px;height:47px">Contate-nos
    <svg viewBox="0 0 16 16"><circle cx="8" cy="8" r="7.5" fill="#fff"/><path d="M6.5 4.5 10 8l-3.5 3.5" stroke="#f37021" stroke-width="2" fill="none"/></svg>
  </a>
</header>

<section class="hero">
  <div class="hero-photo" role="img" aria-label="Sala de espera moderna do consultório com sofás e quadro abstrato"></div>
  <div class="hero-shade"></div>
  <h1 class="hero-title">Cuidar com precisão, tratar com empatia</h1>
  <p class="hero-text">A cirurgia robótica representa um dos avanços mais relevantes da medicina moderna. Ela oferece mais precisão, menor sangramento e uma recuperação mais rápida.</p>
  <a class="btn" href="#" style="left:518px;top:412px;width:164px;height:47px">Saiba mais
    <svg viewBox="0 0 16 16"><circle cx="8" cy="8" r="7.5" fill="#fff"/><path d="M6.5 4.5 10 8l-3.5 3.5" stroke="#f37021" stroke-width="2" fill="none"/></svg>
  </a>
  <div class="arrow" style="left:34px;background:rgba(255,255,255,.15)">
    <svg width="14" height="14" viewBox="0 0 14 14"><path d="M9 2 4 7l5 5" stroke="#fff" stroke-width="2.2" fill="none"/></svg>
  </div>
  <div class="arrow" style="left:1130px;background:#fff">
    <svg width="14" height="14" viewBox="0 0 14 14"><path d="M5 2l5 5-5 5" stroke="#333" stroke-width="2.2" fill="none"/></svg>
  </div>
  <svg class="hero-wave" viewBox="0 0 1200 240" preserveAspectRatio="none">
    <path d="M0 240 L0 200 C110 120 210 90 300 85 C470 80 560 150 760 150 C950 150 1100 90 1200 0 L1200 240 Z" fill="#fff"/>
    <path d="M0 212 C80 140 170 110 280 96" stroke="#0f2238" stroke-width="9" fill="none"/>
    <path d="M1040 130 C1110 110 1160 80 1200 50" stroke="#0f2238" stroke-width="5" fill="none"/>
  </svg>
</section>

<section class="about">
  <div class="abs about-ring"></div>
  <div class="abs about-photo" role="img" aria-label="Retrato do Dr. Rui Valmonte"></div>
  <div class="abs name-badge">
    <span class="dot"><svg width="20" height="20" viewBox="0 0 24 24" fill="#fff"><circle cx="12" cy="7" r="4.5"/><path d="M3 22c0-5 4-8 9-8s9 3 9 8z"/></svg></span>
    Dr. Rui Valmonte
  </div>
  <div class="abs about-text">
    <h2 class="heading">Sobre mim</h2>
    <div class="about-sub">Cuidar com precisão, tratar com empatia</div>
    <p>Sou urologista com foco em cirurgia robótica e atenção integral ao paciente. Mais do que uma técnica, acredito que a boa medicina começa pela escuta, pelo planejamento cuidadoso e pelo compromisso com o que há de melhor para cada pessoa.</p>
    <p>Minha missão é oferecer tratamentos baseados em ciência, tecnologia e humanidade — respeitando o tempo, as escolhas e os objetivos de cada paciente.</p>
  </div>
  <a class="btn" href="#" style="left:641px;top:1237px;width:166px;height:47px">Saiba mais
    <svg viewBox="0 0 16 16"><circle cx="8" cy="8" r="7.5" fill="#fff"/><path d="M6.5 4.5 10 8l-3.5 3.5" stroke="#f37021" stroke-width="2" fill="none"/></svg>
  </a>
</section>

<section class="approach">
  <h2 class="heading">Como atuamos</h2>
  <div class="approach-sub">Nem todo tratamento precisa ser cirúrgico. Nem toda cirurgia precisa ser robótica.</div>
  <div class="approach-text">
    <p>A cirurgia robótica é um grande avanço, mas deve ser indicada com critério. Antes de propor qualquer intervenção, avaliamos o caso de forma ampla:</p>
    <p>Nosso foco é garantir que o paciente seja encaminhado à opção com maior potencial de resultado — seja ela cirúrgica, clínica ou mesmo vigilância ativa.</p>
  </div>

  <div class="card" style="left:110px">
    <div class="card-icon">
      <svg width="58" height="58" viewBox="0 0 48 48" fill="none" stroke="#f37021" stroke-width="2" stroke-linejoin="round" stroke-linecap="round"><path d="M24 24s-9-5.5-9-11a4.5 4.5 0 0 1 9-1.5A4.5 4.5 0 0 1 33 13c0 5.5-9 11-9 11z"/><path d="M24 12v8M20 16h8"/><path d="M4 22l5 16h8M44 22l-5 16h-8M11 28l6 6v8M37 28l-6 6v8"/></svg>
    </div>
    <h3>Utilizamos os guidelines médicos mais atualizados</h3>
  </div>
  <div class="card" style="left:451px">
    <div class="card-icon filled">
      <svg width="58" height="58" viewBox="0 0 48 48" fill="none" stroke="#fff" stroke-width="2" stroke-linejoin="round" stroke-linecap="round"><path d="M14 30a8 8 0 0 1-1-16 11 11 0 0 1 21 2 7 7 0 0 1 0 14z"/><rect x="17" y="18" width="14" height="10" rx="1.5"/><text x="24" y="26" fill="#fff" stroke="none" font-size="7" font-family="Poppins,sans-serif" font-weight="700" text-anchor="middle">AI</text><path d="M24 30v8M14 38h20M14 38v3M34 38v3"/></svg>
    </div>
    <h3>Fazemos uso de ferramentas de inteligência artificial para apoiar a decisão clínica</h3>
  </div>
  <div class="card" style="left:792px">
    <div class="card-icon">
      <svg width="58" height="58" viewBox="0 0 48 48" fill="none" stroke="#f37021" stroke-width="2" stroke-linejoin="round" stroke-linecap="round"><circle cx="24" cy="20" r="10"/><circle cx="24" cy="20" r="4"/><path d="M24 6v3M24 31v3M10 20h3M35 20h3M14 10l2 2M34 10l-2 2M20 34v6h8v-6M21 43h6"/></svg>
    </div>
    <h3>Conduzimos conversas francas sobre as reais necessidades, benefícios e riscos de cada abordagem.</h3>
  </div>
</section>

<section class="services">
  <h2 class="heading">Nossos serviços</h2>
  <div class="tab active" style="left:124px">Planejamento com tecnologia 3D</div>
  <div class="tab" style="left:444px">Apoio pré-procedimento</div>
  <div class="tab" style="left:764px">Cuidado no pós-operatório</div>

  <div class="panel">
    <h3 class="heading">Planejamento com tecnologia 3D</h3>
    <div class="panel-sub">Ver além da imagem: planejar com profundidade.</div>
    <div class="panel-text">
      <p>Em cirurgias renais e prostáticas, adotamos o uso de modelos 3D personalizados, criados a partir dos exames do próprio paciente.</p>
      <p>Esses modelos ajudam a compreender a anatomia de forma precisa, facilitando a escolha da melhor abordagem cirúrgica.</p>
    </div>
    <a class="btn" href="#" style="left:42px;top:376px;width:166px;height:47px">Saiba mais
      <svg viewBox="0 0 16 16"><circle cx="8" cy="8" r="7.5" fill="#fff"/><path d="M6.5 4.5 10 8l-3.5 3.5" stroke="#f37021" stroke-width="2" fill="none"/></svg>
    </a>
    <div class="panel-image" role="img" aria-label="Reconstrução anatômica 3D dos rins e vasos sanguíneos"></div>
  </div>
</section>

<section class="commitment">
  <h2 class="heading">Compromisso com o<br>paciente</h2>
  <div class="commitment-text">
    <p>Acreditamos que o melhor resultado vem da soma entre conhecimento, tecnologia e empatia.<br>Nosso compromisso é entender profundamente o que você está enfrentando, apresentar com clareza todas as opções disponíveis e construir, juntos, o melhor caminho para o seu tratamento.</p>
    <p>Porque cada paciente é único — e merece ser cuidado como tal.</p>
  </div>
  <a class="btn" href="#" style="left:508px;top:3385px;width:183px;height:47px">Contate-nos
    <svg viewBox="0 0 16 16"><circle cx="8" cy="8" r="7.5" fill="#fff"/><path d="M6.5 4.5 10 8l-3.5 3.5" stroke="#f37021" stroke-width="2" fill="none"/></svg>
  </a>
</section>

<footer class="footer">
  <div class="brand">
    <div class="brand-name">Dr Rui Valmonte</div>
    <div class="brand-tag">Urologia e cirurgia minimamente invasiva</div>
  </div>
  <nav class="footer-nav">
    <span>Início</span><span class="sep">|</span><span>Sobre nós</span><span class="sep">|</span><span>Nossos serviços</span><span class="sep">|</span><span>Recursos</span><span class="sep">|</span><span>Contate-nos</span>
  </nav>
  <div class="footer-contact">
    <span><svg width="14" height="14" viewBox="0 0 24 24" fill="#5b3a8e"><path d="M22 16.9v3a2 2 0 0 1-2.2 2 19.8 19.8 0 0 1-8.6-3.1 19.5 19.5 0 0 1-6-6A19.8 19.8 0 0 1 2.1 4.2 2 2 0 0 1 4.1 2h3a2 2 0 0 1 2 1.7c.1.9.4 1.8.7 2.7a2 2 0 0 1-.5 2.1L8 9.8a16 16 0 0 0 6 6l1.3-1.3a2 2 0 0 1 2.1-.4c.9.3 1.8.6 2.7.7a2 2 0 0 1 1.7 2z"/></svg>+1 (555) 014 2290</span>
    <span>|</span>
    <span><svg width="15" height="12" viewBox="0 0 20 16" fill="#5b3a8e"><path d="M0 2a2 2 0 0 1 2-2h16a2 2 0 0 1 2 2v.5L10 9 0 2.5z"/><path d="M0 5l10 6.5L20 5v9a2 2 0 0 1-2 2H2a2 2 0 0 1-2-2z"/></svg>contato@ruivalmonte.pt</span>
  </div>
  <span class="social active" style="left:540px;top:243px"></span>
  <span class="social" style="left:583px;top:243px"></span>
  <span class="social" style="left:626px;top:243px"></span>
  <div class="footer-rule"></div>
  <div class="copyright">© 2025 &nbsp;|&nbsp; Todos os direitos reservados &nbsp;|&nbsp; Termos e Condições</div>
</footer>

</body>
</html>
```